BRMSC redesign and update stationary bc envelopes.

Stationary, Envelopes, Brochures, Business Card. Need to add second surgeon and two other offices. I need everything to match. I am a oral & maxillofacial surgeon.
Additional surgeon and three office addresses.
Tae Woo Park, DMD, MD, INC

3178 Silver Meadow Boulevard
El Dorado Hills, CA 95762

612 Lorel Lane, Suite 101
Folsom, CA. 95630

2375 Birch Avenue, Suite 105
Auburn, CA. 95603
Updates

Logo design uploaded. Zapfino Extra/Adobe Garamond/Palatino are fonts used before. Not sure what is on exisiting stationary.

Target Market(s)

Referral dentist and sometimes patients. I am a oral & Maxillofacial surgeon.

Industry/Entity Type

Dental Clinic

Font styles to use
Serif
Script

Requirements
Must have
• Color of existing stationary. Update is possible.
Nice to have
• Conservative/modern
Should not have
• Playful

```html
<!DOCTYPE html>
<html lang="en">
<head>
<meta charset="utf-8">
<title>BRMSC Stationery Set</title>
<link rel="stylesheet" href="https://fonts.googleapis.com/css2?family=EB+Garamond:ital,wght@0,400;1,400&family=Open+Sans:wght@400;600&display=swap">
<style>
:root{
  --canvas:#dcdcdc;
  --paper:#ffffff;
  --green:#6a8a22;
  --green-text:#5f8a1c;
  --brown:#4e3b2a;
  --body:#3d3d3d;
  --dot:#f1e27a;
  --band-text:#f7f5e6;
  --label:#7a7a7a;
  --rule:#b9a98f;
}
*{margin:0;padding:0;box-sizing:border-box}
html,body{width:1200px;height:769px;overflow:hidden;background:var(--canvas)}
.scene{position:relative;width:1200px;height:769px}
.sheet{position:absolute;background:var(--paper);box-shadow:0 2px 6px rgba(0,0,0,.25);overflow:hidden}
.serif{font-family:"EB Garamond",Garamond,serif}
.sans{font-family:"Open Sans",Arial,sans-serif}
.brand{position:absolute;font-family:"EB Garamond",Garamond,serif;color:var(--brown);letter-spacing:2px;line-height:1}
.contact{position:absolute;font-family:"EB Garamond",Garamond,serif;color:var(--brown);line-height:1.25}
.contact .doctor{color:var(--green-text)}
.contact .row{display:flex;align-items:center;gap:3px;white-space:nowrap}
.contact svg{fill:var(--green-text);flex:none}
.divider{position:absolute;width:0;border-left:1px solid var(--rule)}
.band{position:absolute;left:0;right:0;bottom:0;background:var(--green);color:var(--band-text);
  font-family:"EB Garamond",Garamond,serif;font-style:italic;text-align:center;display:flex;flex-direction:column;justify-content:center}
.band .dot{color:var(--dot);font-style:normal}
.label{position:absolute;left:814px;top:124px;font-family:"Open Sans",Arial,sans-serif;font-size:18px;color:var(--label)}

/* letterhead */
.letterhead{left:86px;top:100px;width:438px;height:560px}
.letter{position:absolute;left:41px;width:355px;font-family:"Open Sans",Arial,sans-serif;font-size:7px;color:var(--body)}
.letter p{line-height:12.6px;text-align:justify}
.signature{position:absolute;left:41px;top:398px;width:100px;height:14px;background:linear-gradient(90deg,#e9e9e9,#f6f6f6)}
.footer-address{position:absolute;left:0;right:0;font-family:"EB Garamond",Garamond,serif;color:var(--brown);font-size:7.6px;text-align:center;line-height:11px}

/* envelope */
.envelope{left:597px;top:171px;width:507px;height:229px}
.website{position:absolute;left:0;right:0;text-align:center;font-family:"EB Garamond",Garamond,serif;color:var(--brown)}

/* cards */
.card-front{left:607px;top:487px;width:233px;height:137px}
.card-back{left:861px;top:487px;width:234px;height:137px}
</style>
</head>
<body>
<svg width="0" height="0" style="position:absolute" aria-hidden="true">
  <symbol id="icon-phone" viewBox="0 0 10 10"><path d="M2 1l2 2-1 1c.6 1.3 1.7 2.4 3 3l1-1 2 2-1.5 1.5C4 9 1 6 .5 2.5z"/></symbol>
  <symbol id="icon-fax" viewBox="0 0 10 10"><path d="M3 0h4v3H3zM1 3h8v5H7v2H3V8H1zM4 7v2h2V7z"/></symbol>
  <symbol id="icon-mail" viewBox="0 0 10 10"><path d="M0 2h10v6H0zM1 3v.3l4 2.6 4-2.6V3L5 5.5z"/></symbol>
  <symbol id="icon-web" viewBox="0 0 10 10"><path d="M5 0a5 5 0 100 10A5 5 0 005 0zm0 1c.8.8 1.2 2 1.3 3.5H3.7C3.8 3 4.2 1.8 5 1zM1.1 5.5h1.6c.1 1.3.4 2.4 1 3.2A4 4 0 011.1 5.5zm0-1A4 4 0 013.7 1.3c-.6.8-.9 1.9-1 3.2zm2.6 1h2.6C6.2 7 5.8 8.2 5 9c-.8-.8-1.2-2-1.3-3.5zm2.6 3.2c.6-.8.9-1.9 1-3.2h1.6a4 4 0 01-2.6 3.2zm1-4.2c-.1-1.3-.4-2.4-1-3.2a4 4 0 012.6 3.2z"/></symbol>
  <symbol id="icon-pin" viewBox="0 0 10 10"><path d="M5 0a3.5 3.5 0 00-3.5 3.5C1.5 6 5 10 5 10s3.5-4 3.5-6.5A3.5 3.5 0 005 0zm0 2a1.5 1.5 0 110 3 1.5 1.5 0 010-3z"/></symbol>
</svg>

<main class="scene">
  <div class="label">Envelope</div>

  <!-- Letterhead -->
  <section class="sheet letterhead">
    <div class="brand" style="left:42px;top:52px;font-size:20px">BRMSC</div>
    <div class="divider" style="left:258px;top:17px;height:68px"></div>
    <div class="contact" style="left:268px;top:15px;font-size:5.8px">
      <div class="doctor" style="font-size:8px">Daniel R. Whitford, DDS, Inc.</div>
      <div>Diplomate of the American Board of</div>
      <div>Oral &amp; Maxillofacial Surgery</div>
      <div class="doctor" style="font-size:8px;margin-top:2px">Tae Woo Park, DMD, MD, INC</div>
      <div>Dental Implant and Oral Surgery</div>
      <div class="row" style="margin-top:4px"><svg width="5" height="5"><use href="#icon-phone"/></svg>916.555.0142&nbsp;&nbsp;&nbsp;<svg width="5" height="5"><use href="#icon-fax"/></svg>916.555.0187</div>
      <div class="row"><svg width="5" height="5"><use href="#icon-mail"/></svg>drwhitford@brmscsurgery.com</div>
      <div class="row"><svg width="5" height="5"><use href="#icon-web"/></svg>www.brmscsurgery.com</div>
    </div>

    <div class="letter" style="top:102px">Issuing Date: May 5, 2018</div>
    <div class="letter" style="top:119px;line-height:8.5px">Name Of Employee Mr. XYZABC<br>Address of Employee<br>Address Line 2 etc..</div>
    <div class="letter" style="top:167px">Dear Mr.XYZABC</div>
    <div class="letter" style="top:191px">
      <p>Lorem Ipsum has been the industry's standard dummy text ever since the 1500s, when an unknown printer took a galley of type and scrambled it to make a type specimen book. It has survived not only five centuries, but also the leap into electronic typesetting, remaining essentially unchanged. It was popularised in the 1960s with the release of Letraset sheets containing Lorem Ipsum passages, and more recently with desktop publishing software like Aldus PageMaker including versions of Lorem Ipsum.</p>
      <p style="margin-top:12.6px">Lorem Ipsum is simply dummy text of the printing and typesetting industry. Lorem Ipsum has been the industry's standard dummy text ever since the 1500s, when an unknown printer took a galley of type and scrambled it to make a type specimen book.</p>
      <p style="margin-top:12.6px">It has survived not only five centuries, but also the leap into electronic typesetting, remaining essentially unchanged. It was popularised in the 1960s with the release of Letraset sheets containing Lorem IpsumIpsum passages.</p>
    </div>
    <div class="letter" style="top:381px">Yours Sincerely</div>
    <div class="signature" role="img" aria-label="Handwritten signature of Marcus Ellery"></div>
    <div class="letter" style="top:417px;font-size:8.5px;font-weight:600">Marcus Ellery</div>
    <div class="letter" style="top:431px">Managing Director</div>

    <div class="brand" style="left:0;right:0;top:468px;text-align:center;font-size:19px">BRMSC</div>
    <div class="footer-address" style="top:501px">612 Lorel Lane, Suite 101 , Folsom, CA. 95630 <svg width="7" height="8" style="fill:var(--brown);vertical-align:-1px"><use href="#icon-pin"/></svg> 2375 Birch Avenue, Suite 105, Auburn, CA. 95603<br>3178 Silver Meadow Boulevard, El Dorado Hills, CA 95762</div>
    <div class="band" style="height:36px;font-size:8px;line-height:10px">
      <div>Dentoalveolar Surgery <span class="dot">●</span> Dental Implant Surgery <span class="dot">●</span> Orthognathic Surgery <span class="dot">●</span> Facial Trauma Surgery</div>
      <div>Preprosthetic and Reconstructive Surgery <span class="dot">●</span> TMJ Disorders and Surgery <span class="dot">●</span> Obstructive Sleep Apnea Surgery</div>
    </div>
  </section>

  <!-- Envelope -->
  <section class="sheet envelope">
    <div class="brand" style="left:34px;top:62px;font-size:24px">BRMSC</div>
    <div class="divider" style="left:155px;top:18px;height:79px"></div>
    <div class="contact" style="left:168px;top:17px;font-size:6.3px">
      <div class="doctor" style="font-size:8.3px">Daniel R. Whitford, DDS, Inc.</div>
      <div>Diplomate of the American Board of</div>
      <div>Oral &amp; Maxillofacial Surgery</div>
      <div class="doctor" style="font-size:8.3px;margin-top:3px">Tae Woo Park, DMD, MD, INC</div>
      <div>Dental Implant and Oral Surgery</div>
      <div class="row" style="margin-top:5px"><svg width="5" height="6"><use href="#icon-pin"/></svg>3178 Silver Meadow Boulevard, El Dorado Hills, CA 95762</div>
      <div class="row" style="margin-top:2px"><svg width="5" height="6"><use href="#icon-pin"/></svg>612 Lorel Lane, Suite 101 , Folsom, CA. 95630</div>
      <div class="row" style="margin-top:2px"><svg width="5" height="6"><use href="#icon-pin"/></svg>2375 Birch Avenue, Suite 105, Auburn, CA. 95603</div>
    </div>
    <div class="website" style="top:170px;font-size:9.5px;letter-spacing:2px">www.brmscsurgery.com</div>
    <div class="band" style="height:42px;font-size:8.6px;line-height:10.5px">
      <div>Dentoalveolar Surgery <span class="dot">●</span> Dental Implant Surgery <span class="dot">●</span> Orthognathic Surgery <span class="dot">●</span> Facial Trauma Surgery</div>
      <div>Preprosthetic and Reconstructive Surgery <span class="dot">●</span> TMJ Disorders and Surgery <span class="dot">●</span> Obstructive Sleep Apnea Surgery</div>
    </div>
  </section>

  <!-- Business card front -->
  <section class="sheet card-front">
    <div class="brand" style="left:14px;top:60px;font-size:16px">BRMSC</div>
    <div class="contact" style="left:103px;top:16px;font-size:5.7px">
      <div class="doctor" style="font-size:8px">Daniel R. Whitford, DDS, Inc.</div>
      <div>Diplomate of the American Board of</div>
      <div>Oral &amp; Maxillofacial Surgery</div>
      <div class="doctor" style="font-size:8px;margin-top:3px">Tae Woo Park, DMD, MD, INC</div>
      <div>Dental Implant and Oral Surgery</div>
      <div class="row" style="margin-top:5px"><svg width="5" height="5"><use href="#icon-phone"/></svg>916.555.0142&nbsp;&nbsp;&nbsp;<svg width="5" height="5"><use href="#icon-fax"/></svg>916.555.0187</div>
      <div class="row" style="margin-top:1px"><svg width="5" height="5"><use href="#icon-mail"/></svg>drwhitford@brmscsurgery.com</div>
      <div class="row" style="margin-top:1px"><svg width="5" height="5"><use href="#icon-web"/></svg>www.brmscsurgery.com</div>
    </div>
    <div class="band" style="height:22px;font-size:7px;letter-spacing:1.5px">
      <div>www.brmscsurgery.com</div>
    </div>
  </section>

  <!-- Business card back -->
  <section class="sheet card-back">
    <div class="brand" style="left:0;right:0;top:26px;text-align:center;font-size:18px">BRMSC</div>
    <svg style="position:absolute;left:76px;top:52px" width="82" height="8" aria-hidden="true">
      <line x1="0" y1="4" x2="34" y2="4" stroke="var(--brown)" stroke-width=".6"/>
      <use href="#icon-pin" x="37" y="0" width="8" height="8" fill="var(--brown)"/>
      <line x1="48" y1="4" x2="82" y2="4" stroke="var(--brown)" stroke-width=".6"/>
    </svg>
    <div class="footer-address" style="top:62px;font-size:6.3px;line-height:8.5px">3178 Silver Meadow Boulevard El Dorado Hills, CA 95762<br>2375 Birch Avenue, Suite 105 Auburn, CA. 95603<br>612 Lorel Lane, Suite 101 Folsom, CA. 95630</div>
    <div class="band" style="height:38px;font-size:6.1px;line-height:7px">
      <div>Dentoalveolar Surgery <span class="dot">●</span> Dental Implant Surgery <span class="dot">●</span> Orthognathic Surgery</div>
      <div>Facial Trauma Surgery <span class="dot">●</span> Preprosthetic and Reconstructive Surgery</div>
      <div>TMJ Disorders and Surgery <span class="dot">●</span> Obstructive Sleep Apnea Surgery</div>
    </div>
  </section>
</main>
</body>
</html>
```